business card design for luxurious real estate brand

using the attached logo, i am looking for a 2-sided business card design. the back should be the gold logo on black background. the front needs to include: gold logo, name, phone, email, and website

Industry/Entity Type

real estate

Contact Information for Business Card

logo, name, email, phone, website

Font styles to use
Sans Serif

```html
<!DOCTYPE html>
<html lang="en">
<head>
<meta charset="UTF-8">
<title>Harbor Vale – Business Card</title>
<link rel="stylesheet" href="https://fonts.googleapis.com/css2?family=Archivo:wdth,wght@62..125,400..800&display=swap">
<style>
  :root {
    --backdrop: #161616;
    --card: #040507;
    --gold: #ffd01f;
    --grey: #8b8b8d;
    --rule: #6d6d6f;
  }
  * { margin: 0; padding: 0; box-sizing: border-box; }
  html, body {
    width: 1200px;
    height: 1200px;
    overflow: hidden;
    background: var(--backdrop);
    font-family: "Archivo", Arial, sans-serif;
    font-stretch: 125%;
  }
  .sheet {
    position: relative;
    width: 1200px;
    height: 1200px;
  }
  .card {
    position: absolute;
    left: 356px;
    width: 488px;
    height: 280px;
    background: var(--card);
  }
  .card--front { top: 287px; }
  .card--back  { top: 682px; }

  /* Front */
  .brand-tag {
    position: absolute;
    left: 30px;
    top: 34px;
    display: flex;
    align-items: center;
    gap: 12px;
    color: var(--gold);
    font-weight: 700;
    font-size: 22px;
    letter-spacing: 0.04em;
    text-transform: uppercase;
  }
  .brand-square {
    width: 18px;
    height: 18px;
    background: var(--gold);
  }
  .holder {
    position: absolute;
    right: 31px;
    top: 30px;
    text-align: right;
  }
  .holder__name {
    color: var(--gold);
    font-weight: 800;
    font-size: 32px;
    line-height: 1.22;
    text-transform: uppercase;
  }
  .holder__role {
    margin-top: 10px;
    color: var(--grey);
    font-weight: 700;
    font-size: 11px;
    letter-spacing: 0.36em;
    margin-right: -0.36em;
    text-transform: uppercase;
  }
  .contact {
    position: absolute;
    left: 0;
    right: 31px;
    top: 218px;
    color: var(--grey);
    font-weight: 500;
    font-size: 14px;
  }
  .contact__rule {
    position: absolute;
    left: 44px;
    width: 235px;
    top: 10px;
    height: 1px;
    background: var(--rule);
  }
  .contact__email {
    position: absolute;
    right: 209px;
    top: 22px;
    white-space: nowrap;
  }
  .contact__phone {
    position: absolute;
    right: 0;
    top: 0;
    font-weight: 600;
    font-size: 13px;
    white-space: nowrap;
  }
  .contact__web {
    position: absolute;
    right: 0;
    top: 22px;
    white-space: nowrap;
  }

  /* Back */
  .brand-lockup {
    position: absolute;
    inset: 0;
    display: flex;
    align-items: center;
    justify-content: center;
    gap: 16px;
    color: var(--gold);
    font-weight: 700;
    font-size: 26px;
    letter-spacing: 0.22em;
    text-transform: uppercase;
  }
  .brand-lockup .brand-square {
    width: 22px;
    height: 22px;
  }
</style>
</head>
<body>
  <main class="sheet">
    <section class="card card--front" aria-label="Business card front">
      <div class="brand-tag">
        <span class="brand-square"></span>
        <span>Harbor Vale</span>
      </div>
      <div class="holder">
        <h1 class="holder__name">Mark<br>Ellison</h1>
        <p class="holder__role">Real Estate</p>
      </div>
      <div class="contact">
        <span class="contact__rule"></span>
        <span class="contact__email">mark@harborvale.com</span>
        <span class="contact__phone">+1 555–010–4477</span>
        <span class="contact__web">harborvale.com</span>
      </div>
    </section>

    <section class="card card--back" aria-label="Business card back">
      <div class="brand-lockup">
        <span class="brand-square"></span>
        <span>Harbor Vale</span>
      </div>
    </section>
  </main>
</body>
</html>
```